valtheon construction

i want a construction website something that really epic and eye catchy

we do full Renovation Restoration Construction

if anyone can make my jaw drop there well be a big Reward ,

i have attach my logo

Industry/Entity Type

Construction

Number of Pages Required

4 page

```html
<!DOCTYPE html>
<html lang="en">
<head>
<meta charset="utf-8">
<title>Valtheon Construction</title>
<link rel="stylesheet" href="https://fonts.googleapis.com/css2?family=Arimo:wght@400;700&family=PT+Serif:wght@400;700&display=swap">
<style>
  :root {
    --red: #b3141d;
    --red-deep: #8c0d13;
    --red-band: #a6131b;
    --ink: #333333;
    --muted: #888888;
    --paper: #ffffff;
    --footer: #2a2a2a;
    --footer-field: #1c1c1c;
    --panel-line: #c9c9c9;
    --sans: "Arimo", Arial, sans-serif;
    --serif: "PT Serif", Georgia, serif;
  }
  * { box-sizing: border-box; margin: 0; padding: 0; }
  html, body { width: 800px; height: 1200px; overflow: hidden; background: var(--paper); }
  body { position: relative; font-family: var(--sans); color: var(--ink); }

  .site-header { position: absolute; left: 0; top: 0; width: 800px; height: 96px; border-bottom: 4px solid var(--red-deep); }
  .brand { position: absolute; left: 18px; top: 14px; display: flex; align-items: center; gap: 8px; }
  .brand-mark { width: 30px; height: 30px; background: var(--red); }
  .brand-name { font-family: var(--sans); font-weight: 700; color: var(--red); line-height: 1; }
  .brand-name .big { display: block; font-size: 24px; letter-spacing: 0.5px; }
  .brand-name .small { display: block; font-size: 11px; margin-top: 2px; letter-spacing: 0.6px; }

  .search { position: absolute; right: 20px; top: 22px; display: flex; }
  .search-field { width: 170px; height: 22px; background: #3a3a3a; color: #bbb; font-size: 10px; padding: 5px 8px; }
  .search-btn { width: 52px; height: 22px; background: var(--red); color: #fff; font-size: 10px; text-align: center; line-height: 22px; }

  .main-nav { position: absolute; right: 16px; top: 70px; display: flex; }
  .main-nav a { font-size: 11px; color: var(--red); text-decoration: none; padding: 0 9px; border-left: 1px solid #ddd; }
  .main-nav a:first-child { border-left: none; }

  .welcome { position: absolute; top: 106px; left: 0; width: 800px; text-align: center; font-size: 25px; font-weight: 700; color: var(--red-deep); letter-spacing: 0.3px; }
  .welcome-bar { position: absolute; top: 140px; left: 0; width: 800px; height: 6px; background: var(--red-deep); }

  .hero { position: absolute; top: 146px; left: 0; width: 800px; height: 362px;
    background:
      radial-gradient(ellipse 220px 150px at 120px 120px, rgba(40,42,44,0.85), rgba(40,42,44,0) 100%),
      radial-gradient(ellipse 260px 90px at 190px 320px, rgba(250,250,250,0.9), rgba(250,250,250,0) 100%),
      radial-gradient(ellipse 200px 60px at 650px 265px, rgba(255,255,255,0.95), rgba(255,255,255,0) 100%),
      radial-gradient(ellipse 160px 120px at 560px 150px, rgba(70,72,76,0.6), rgba(70,72,76,0) 100%),
      linear-gradient(180deg, #6f7174 0%, #b9babc 35%, #e6e6e7 60%, #8d8e90 100%); }

  .features { position: absolute; top: 528px; left: 22px; width: 756px; display: flex; justify-content: space-between; }
  .feature { width: 232px; display: flex; gap: 10px; }
  .feature-thumb { width: 68px; height: 68px; flex: none; background: #3a3a3a; color: #fff; font-size: 9px; display: flex; align-items: center; justify-content: center; }
  .feature-title { font-family: var(--serif); font-size: 10px; color: var(--red); margin-bottom: 4px; }
  .feature-text { font-size: 7.5px; line-height: 1.5; color: var(--muted); }

  .showcase { position: absolute; top: 640px; left: 0; width: 800px; height: 362px;
    background: linear-gradient(180deg, #b8161f 0%, var(--red-band) 60%, #93111a 100%); border-top: 6px solid #dedede; }
  .showcase-tab { position: absolute; top: 10px; left: 295px; width: 210px; height: 36px; background: var(--paper); border-radius: 10px; text-align: center; line-height: 36px; font-size: 23px; color: var(--red); }
  .slider-arrow { position: absolute; top: 156px; width: 18px; height: 34px; background: #e3e3e3; border: 1px solid #bdbdbd; }
  .slider-arrow.prev { left: 76px; }
  .slider-arrow.next { right: 76px; }
  .slider-arrow svg { display: block; margin: 11px auto 0; }
  .slider { position: absolute; top: 66px; left: 92px; width: 616px; height: 262px; background: #e8e8e8; border: 1px solid var(--panel-line); border-radius: 10px; padding: 8px; }
  .slider-stage { width: 100%; height: 198px; background: var(--paper); border: 1px solid #d4d4d4; border-radius: 6px; position: relative; }
  .loader { position: absolute; top: 86px; left: 160px; display: flex; align-items: center; gap: 10px; }
  .loader-box { width: 80px; height: 26px; border: 1px solid #ccc; border-radius: 4px; display: flex; align-items: center; gap: 6px; padding-left: 6px; font-size: 10px; color: #666; }
  .progress { width: 150px; height: 14px; border: 1px solid #bbb; border-radius: 3px; background: #f2f2f2; }
  .progress span { display: block; width: 75%; height: 100%; background: linear-gradient(#c8d0d8, #9aa6b2); }
  .loader-value { font-size: 9px; color: #666; }
  .pager { display: flex; gap: 8px; margin-top: 12px; padding: 0 4px; }
  .pager span { height: 22px; min-width: 22px; padding: 0 8px; border: 1px solid #c0c0c0; border-radius: 4px; background: #f7f7f7; font-size: 10px; color: #555; line-height: 20px; text-align: center; }
  .pager .wide { min-width: 40px; }
  .pager .gap { margin-left: auto; }
  .pager .ok { background: #9a9a9a; color: #fff; border-color: #8a8a8a; }

  .site-footer { position: absolute; top: 1002px; left: 0; width: 800px; height: 198px; background: var(--footer); display: flex; padding: 22px 16px 0; gap: 22px; }
  .footer-col { width: 178px; }
  .footer-col h3 { font-family: var(--serif); font-weight: 400; font-size: 15px; color: #fff; margin-bottom: 12px; }
  .footer-col p, .footer-col li { font-size: 8px; line-height: 1.75; color: #d2313a; list-style: none; }
  .quick-links li { border-bottom: 1px solid #4a4a4a; padding: 2px 0; }
  .blog-title { font-family: var(--serif); font-style: italic; color: #ccc !important; }
  .blog-meta, .blog-text { color: #999 !important; }
  .read-more { text-align: right; color: #d2313a !important; }
  .field { width: 170px; height: 18px; background: var(--footer-field); border: 1px solid #444; font-size: 8px; color: #aaa; padding: 3px 6px; margin-bottom: 6px; }
  .submit { width: 46px; height: 18px; background: var(--red); color: #fff; font-size: 8px; text-align: center; line-height: 18px; }
</style>
</head>
<body>
  <header class="site-header">
    <div class="brand">
      <div class="brand-mark"></div>
      <div class="brand-name"><span class="big">VALTHEON</span><span class="small">CONSTRUCTION CO.</span></div>
    </div>
    <div class="search"><div class="search-field">Search Our Website...</div><div class="search-btn">SEARCH</div></div>
    <nav class="main-nav">
      <a href="#">HOME</a><a href="#">ABOUT US</a><a href="#">SERVICES</a><a href="#">NEWS</a><a href="#">PORTFOLIO</a><a href="#">CONTACT US</a>
    </nav>
  </header>

  <h1 class="welcome">WELCOME TO VALTHEON CONSTRUCTION</h1>
  <div class="welcome-bar"></div>

  <div class="hero" role="img" aria-label="Bright modern interior of a renovated living and dining room with white furniture and large windows"></div>

  <section class="features">
    <article class="feature">
      <div class="feature-thumb">In a Scope</div>
      <div><h4 class="feature-title">Title Goes Here</h4>
        <p class="feature-text">We rebuild worn homes with care, keeping every beam true and every finish clean for lasting years.</p></div>
    </article>
    <article class="feature">
      <div class="feature-thumb">In a Scope</div>
      <div><h4 class="feature-title">Title Goes Here</h4>
        <p class="feature-text">Our restoration crews bring old facades back to life with honest materials and patient, skilled hands.</p></div>
    </article>
    <article class="feature">
      <div class="feature-thumb">In a Scope</div>
      <div><h4 class="feature-title">Title Goes Here</h4>
        <p class="feature-text">From first sketch to final key, we build new spaces on time, on budget and built to last.</p></div>
    </article>
  </section>

  <section class="showcase">
    <div class="showcase-tab">Best Construction</div>
    <div class="slider">
      <div class="slider-stage">
        <div class="loader">
          <div class="loader-box">
            <svg width="12" height="12" viewBox="0 0 12 12"><circle cx="6" cy="6" r="4.5" fill="none" stroke="#bbb" stroke-width="1.5"/><path d="M6 1.5 A4.5 4.5 0 0 1 10.5 6" fill="none" stroke="#777" stroke-width="1.5"/></svg>
            loading
          </div>
          <div class="progress"><span></span></div>
          <div class="loader-value">75%</div>
        </div>
      </div>
      <div class="pager">
        <span class="wide">first</span><span>‹</span><span>1</span><span>2</span><span>3</span><span>4</span><span>›</span><span class="wide">last</span>
        <span class="wide gap">cancel</span><span class="wide ok">ok</span>
      </div>
    </div>
    <div class="slider-arrow prev"><svg width="6" height="10" viewBox="0 0 6 10"><path d="M5 1 L1 5 L5 9" fill="none" stroke="#777" stroke-width="1.5"/></svg></div>
    <div class="slider-arrow next"><svg width="6" height="10" viewBox="0 0 6 10"><path d="M1 1 L5 5 L1 9" fill="none" stroke="#777" stroke-width="1.5"/></svg></div>
  </section>

  <footer class="site-footer">
    <div class="footer-col">
      <h3>Contact Details</h3>
      <p>14 Harrowgate Road</p>
      <p>Marlow Street Building</p>
      <p>Suite 400, Ellbridge</p>
      <p>Tel: 555 0142 880</p>
      <p>info@valtheonbuild.test</p>
    </div>
    <div class="footer-col quick-links">
      <h3>Quick Links</h3>
      <ul><li>Our Services</li><li>Our Projects</li><li>Testimonials</li><li>Contact Us</li></ul>
    </div>
    <div class="footer-col">
      <h3>From The Blog</h3>
      <p class="blog-title">Blog Post Title</p>
      <p class="blog-meta">Posted by admin on 12.04</p>
      <p class="blog-text">Simple tips for planning a home renovation that stays on schedule and within budget.</p>
      <p class="read-more">Read More</p>
    </div>
    <div class="footer-col">
      <h3>Newsletter</h3>
      <div class="field">Name</div>
      <div class="field">Email</div>
      <div class="submit">SUBMIT</div>
    </div>
  </footer>
</body>
</html>
```